Zielgruppe
Unsere Firma produziert individuelles Büromaterialen aus Papier & Kunststoff (bspw. Ringbücher, Klarsichthüllen, Mappen, etc.) Zielgruppe sind (eher konservative) Unternehmenskunden in allen Branchen (speziell Logistik, KFZ, Gesundheit).
Die Broschüre soll primär zur Neukundenakquise als auch für Neuverkäufe an Bestandskunden verwendet werden und in einem schlichten, modernen und hochwertigen Design eine Übersicht über unser Produktportfolio bieten.
Aufgabenstellung
Die Broschüre soll auf Basis des bestehenden Corporate Designs gestaltet werden.
1) In der Broschüre soll jede unserer fünf Produktkategorien (Ordner, Ringbuchordner, Ordnerregister, Hüllen & Taschen, Mappen) eine eigene Seite/Abschnitt erhalten, ähnlich unserer Website.
2) Zudem soll auf einer eigenen Seite/Abschnitt prägnant darauf hingewiesen werden, dass wir für alle Produktkategorie individuelle Sonderanfertigungen anbieten.
Die Strukturierung und Aufteilung der Inhalt in der Broschüre soll sich relativ klar an unserer Website orientieren. Medien & bereits vorhandene Texte sind sowohl als Anlage dem Projekt beigefügt, als auch auf unserer Website auffindbar. Falls notwendig wären wir auch bereit zu einzelnen Themenbereiche neue Texte erstellen zu lassen.
Hinsichtlich des Formats überlassen wir die Auswahl dem Designer. Die Broschüre wird jedoch auch häufig in digitaler Form versandt.

```html
<!DOCTYPE html>
<html lang="de">
<head>
<meta charset="utf-8">
<title>Produktübersicht 2022 – Umschlag</title>
<link rel="stylesheet" href="https://fonts.googleapis.com/css2?family=Michroma&display=swap">
<style>
  :root {
    --bg: #a3aab1;
    --paper: #fbfbfb;
    --brand-blue: #1b3f8b;
    --band: #d3d9e6;
    --band-glass: rgba(214, 220, 234, 0.85);
    --ink: #4a4d55;
    --photo-light: #e6e4e2;
    --photo-mid: #cfc6bb;
    --photo-dark: #a8998a;
  }
  * { box-sizing: border-box; margin: 0; padding: 0; }
  html, body { width: 1200px; height: 960px; overflow: hidden; }
  body {
    background: var(--bg);
    font-family: "Michroma", sans-serif;
    color: var(--ink);
  }
  .spread {
    position: absolute;
    left: 80px; top: 112px;
    width: 1040px; height: 736px;
    display: flex;
    box-shadow: 0 14px 40px rgba(40, 48, 58, 0.25);
  }
  .page {
    position: relative;
    width: 520px; height: 736px;
    background: var(--paper);
    overflow: hidden;
  }
  .page svg.layer { position: absolute; inset: 0; }

  .brand {
    position: absolute;
    display: flex; align-items: center; gap: 8px;
    color: var(--brand-blue);
  }
  .brand-mark { width: 11px; height: 11px; border-radius: 50%; background: var(--brand-blue); }
  .brand-name { font-size: 13px; letter-spacing: 0.5px; }

  /* back cover */
  .back .brand { left: 44px; top: 566px; }
  .contact {
    position: absolute; left: 56px; top: 612px;
    font-size: 8px; line-height: 1.65; font-style: normal; color: var(--ink);
  }
  .contact .company { color: var(--brand-blue); }

  /* front cover */
  .front .brand { right: 40px; top: 40px; }
  .headline {
    position: absolute; left: 90px; top: 408px;
    font-size: 21px; font-weight: 400; line-height: 1.45; color: var(--brand-blue);
  }
  .subline {
    position: absolute; left: 92px; top: 492px;
    font-size: 9px; letter-spacing: 1.2px; color: var(--ink);
  }
</style>
</head>
<body>
<main class="spread">

  <section class="page back" aria-label="Rückseite">
    <svg class="layer" width="520" height="736" viewBox="0 0 520 736">
      <path d="M0 560 Q260 545 520 470 L520 640 Q260 690 0 700 Z" fill="var(--band)"/>
    </svg>
    <div class="brand"><span class="brand-mark"></span><span class="brand-name">Verondo</span></div>
    <address class="contact">
      <div class="company">Verondo UG Papier-<br>&amp; Kunststoffverarbeitung</div>
      Lindenweg 12<br>
      40210 Musterstadt<br>
      Telefon: +49211 5550 140<br>
      E-Mail: kontakt@verondo.de
    </address>
  </section>

  <section class="page front" aria-label="Titelseite">
    <svg class="layer" width="520" height="736" viewBox="0 0 520 736">
      <defs>
        <linearGradient id="photoTone" x1="0" y1="0" x2="1" y2="1">
          <stop offset="0" stop-color="var(--photo-mid)"/>
          <stop offset="0.35" stop-color="var(--photo-light)"/>
          <stop offset="0.7" stop-color="var(--photo-dark)"/>
          <stop offset="1" stop-color="var(--photo-light)"/>
        </linearGradient>
      </defs>
      <path role="img" aria-label="Foto: geöffneter Ringbuchordner mit Metallmechanik"
            d="M0 150 Q280 165 520 85 L520 736 L0 736 Z" fill="url(#photoTone)"/>
      <rect x="486" y="92" width="18" height="250" fill="var(--brand-blue)"/>
      <path d="M0 395 Q280 385 520 340 L520 500 Q280 560 0 575 Z" fill="var(--band-glass)"/>
      <rect x="486" y="505" width="18" height="70" fill="var(--brand-blue)"/>
    </svg>
    <div class="brand"><span class="brand-mark"></span><span class="brand-name">Verondo</span></div>
    <h1 class="headline">Papier und Kunststoff<br>sind unser Ding!</h1>
    <p class="subline">PRODUKTÜBERSICHT 2022</p>
  </section>

</main>
</body>
</html>
```